QLDR Individual and Corporate Development Business Card Design

QLDR needs a business card design that is aligned with it's values and targetted markets. Harmonic Ladder of Reasoning Matrix's self diagnosis model and tools, which can be used for personal improvement and team/business performance enhancement, is based on the learnings of over 20 years of medical practitioning. QLDR supercharges personal effectiveness and awareness to also increase team and business performance.

The targetted markets are high performance individuals and teams who aspire seek to enhance their capabilities and achieve their absolute best potential.

Look and feel for the business card design we are looking for is high technology, premium, fresh, new and medical.

Target Market(s)

Industry/Entity Type

Business Consultant

Contact Information for Business Card

Logo, Full Name, Title, Phone number, Email, company name, Address,

Font styles to use
Sans Serif

Requirements
Must have
• Tag line: Clearer Thinking and Stronger Results for Every Team
• Please use same colours as the logo.

```html
<!DOCTYPE html>
<html lang="en">
<head>
<meta charset="UTF-8">
<title>QLDR Business Card</title>
<link rel="stylesheet" href="https://fonts.googleapis.com/css2?family=Roboto:ital,wght@0,400;0,500;0,700;0,900;1,400&family=Roboto+Condensed:wght@700&display=swap">
<style>
  :root {
    --backdrop: #2a2b2d;
    --card: #1d1e20;
    --card-edge: #252628;
    --teal: #1fb6cc;
    --white: #f4f6f7;
  }
  * { box-sizing: border-box; margin: 0; padding: 0; }
  html, body {
    width: 1200px; height: 900px; overflow: hidden;
    background: var(--backdrop);
    font-family: "Roboto", Arial, sans-serif;
  }
  .stage { position: relative; width: 1200px; height: 900px; }
  .card {
    position: absolute; left: 280px; width: 640px; height: 366px;
    background: var(--card);
    border: 1px solid var(--card-edge);
    box-shadow: 0 14px 34px rgba(0,0,0,0.45);
  }
  .card-front { top: 70px; }
  .card-back { top: 470px; }

  /* Front */
  .brand {
    position: absolute; top: 74px; left: 0; right: 0;
    text-align: center; color: var(--teal); font-weight: 700;
  }
  .brand-mark { font-size: 80px; font-weight: 900; line-height: 1; letter-spacing: 8px; }
  .brand-name { margin-top: 10px; font-size: 18px; letter-spacing: 1.2px; text-transform: uppercase; }
  .tagline {
    position: absolute; top: 262px; left: 0; right: 0;
    text-align: center; color: var(--white);
    font-style: italic; font-size: 17px; letter-spacing: 0.3px;
  }

  /* Back */
  .person {
    position: absolute; top: 108px; right: 378px; text-align: right;
  }
  .person-name {
    font-family: "Roboto Condensed", "Arial Narrow", sans-serif;
    font-weight: 700;
    color: var(--teal); font-size: 40px; line-height: 1; letter-spacing: 0.3px;
  }
  .person-title { margin-top: 8px; color: var(--white); font-size: 18px; font-weight: 500; }
  .divider {
    position: absolute; top: 78px; left: 284px; width: 2px; height: 142px;
    background: linear-gradient(to bottom, rgba(255,255,255,0), rgba(255,255,255,0.85) 50%, rgba(255,255,255,0));
  }
  .company {
    position: absolute; top: 98px; left: 312px;
    color: var(--white); font-weight: 700; font-size: 16px; line-height: 1.25;
  }
  .contacts {
    position: absolute; top: 158px; left: 312px; list-style: none;
  }
  .contact-item {
    display: flex; align-items: center; gap: 10px;
    color: var(--white); font-size: 17px; font-weight: 500; height: 23px;
  }
  .icon { width: 15px; height: 15px; fill: var(--teal); flex: none; }
  .address {
    position: absolute; top: 290px; left: 90px;
    display: flex; align-items: center; gap: 10px;
    color: var(--white); font-size: 18px; font-weight: 500;
  }
  .address .icon { width: 16px; height: 20px; }
</style>
</head>
<body>
<main class="stage">
  <section class="card card-front" aria-label="Card front">
    <div class="brand">
      <div class="brand-mark">QLDR</div>
      <div class="brand-name">Harmonic Ladder of Reasoning Matrix</div>
    </div>
    <p class="tagline">Clearer Thinking and Stronger Results for Every Team</p>
  </section>

  <section class="card card-back" aria-label="Card back">
    <div class="person">
      <div class="person-name">ELLIOT MARSH</div>
      <div class="person-title">CEO/FOUNDER</div>
    </div>
    <div class="divider"></div>
    <div class="company">Harmonic Ladder of<br>Reasoning Matrix</div>
    <ul class="contacts">
      <li class="contact-item">
        <svg class="icon" viewBox="0 0 24 24"><path d="M6.6 10.8a15.1 15.1 0 0 0 6.6 6.6l2.2-2.2c.3-.3.7-.4 1-.2 1.1.4 2.3.6 3.6.6.6 0 1 .4 1 1V20c0 .6-.4 1-1 1C10.6 21 3 13.4 3 4c0-.6.4-1 1-1h3.5c.6 0 1 .4 1 1 0 1.3.2 2.5.6 3.6.1.3 0 .7-.2 1z"/></svg>
        555 218 4406
      </li>
      <li class="contact-item">
        <svg class="icon" viewBox="0 0 24 24"><path d="M2 5h20v2l-10 6L2 7z"/><path d="M2 9l10 6 10-6v10H2z"/></svg>
        hello@qldrmatrix.com
      </li>
      <li class="contact-item">
        <svg class="icon" viewBox="0 0 24 24"><circle cx="12" cy="12" r="10"/></svg>
        www.qldrmatrix.com
      </li>
    </ul>
    <div class="address">
      <svg class="icon" viewBox="0 0 24 30"><path d="M12 0C5.4 0 0 5.3 0 11.8 0 20.6 12 30 12 30s12-9.4 12-18.2C24 5.3 18.6 0 12 0zm0 16.5a4.6 4.6 0 1 1 0-9.2 4.6 4.6 0 0 1 0 9.2z"/></svg>
      218 Cedar Ridge Road, Juneau, Alaska 99801
    </div>
  </section>
</main>
</body>
</html>
```